lumineaux project business card, interior design and decoration firm

I'm a young woman and I've just created my interior design consulting firm. I'm very inspired by brasilian design, italian design, argentinian spirit, I like pure forms, chic colors (blue specially) and raw stuffs (wood, glass,
I work with wines properties, boats and yachts dealers, private people. Elegant but inspired
It's very important to dedicate one side to this card to the name Lumineaux. I would like my name on the other side (Claire-Anne Vostel), my mail cavostel@mailrivo.com, my number + 33 6 12 58 39 91

Target Market(s)

middle and upper class, young people,

Contact Information for Business Card

Font styles to use
Sans Serif

Colors
0255a3
85abd2
000000
fdfdfd
86cfc6
fdf0f6
00a990
f04a50

Requirements
Must have
• The name Lumineaux, my name my number and mail one or two colors max, one logo if it's possible. AND uder The name Lumineaux "Cabinet de conseil en aménagement intérieur"

```html
<!DOCTYPE html>
<html lang="fr">
<head>
<meta charset="utf-8">
<title>Lumineaux — carte de visite</title>
<link href="https://fonts.googleapis.com/css2?family=Quicksand:wght@400;500;600&display=swap" rel="stylesheet">
<style>
  :root {
    --backdrop: #d3d3d5;
    --card: #fdfdfd;
    --ink: #1d1d1f;
    --ink-soft: #3a3a3e;
    --brand-blue: #0255a3;
    --soft-blue: #85abd2;
    --stone: #d8d3d1;
    --rule: #6b6b70;
  }
  * { box-sizing: border-box; margin: 0; padding: 0; }
  html, body {
    width: 1200px; height: 932px; overflow: hidden;
    background: var(--backdrop);
    font-family: "Quicksand", sans-serif;
    color: var(--ink);
  }
  .sheet {
    position: relative; width: 1200px; height: 932px;
    display: flex; align-items: center; justify-content: center; gap: 40px;
  }
  .card {
    position: relative; width: 540px; height: 340px;
    background: var(--card); border-radius: 18px; overflow: hidden;
    box-shadow: 0 10px 28px rgba(0,0,0,.16);
  }
  .card__pattern { position: absolute; inset: 0; width: 540px; height: 340px; }
  .brand {
    position: absolute; text-align: left;
  }
  .brand__name {
    display: flex; align-items: center; gap: 8px;
    font-weight: 600; font-size: 30px; color: var(--brand-blue); letter-spacing: .5px;
  }
  .brand__mark { width: 14px; height: 14px; background: var(--brand-blue); }
  .brand__tagline {
    margin-top: 4px; font-weight: 500; font-size: 11.5px; line-height: 1.25; color: var(--ink-soft);
  }
  .card--front .brand { left: 170px; top: 120px; }
  .card--back .brand { left: 180px; top: 30px; }
  .card--back .brand__name { font-size: 24px; }
  .card--back .brand__tagline { font-size: 10px; }
  .rule { position: absolute; height: 1px; background: var(--rule); }
  .rule--top { left: 230px; top: 128px; width: 280px; }
  .rule--bottom { left: 60px; top: 248px; width: 260px; }
  .person { position: absolute; left: 120px; top: 126px; }
  .person__name { font-size: 25px; font-weight: 500; color: var(--ink); }
  .person__name .surname { color: var(--brand-blue); }
  .person__role { margin-left: 70px; font-size: 15px; color: var(--ink-soft); }
  .contact { position: absolute; left: 180px; top: 196px; list-style: none; }
  .contact__item { display: flex; align-items: center; gap: 12px; font-size: 15px; height: 24px; }
  .contact__icon { width: 18px; height: 18px; flex: none; }
</style>
</head>
<body>
<main class="sheet">
  <section class="card card--front" aria-label="Recto Lumineaux">
    <svg class="card__pattern" role="img" aria-label="Motif géométrique de triangles gris" viewBox="0 0 540 340">
      <polygon points="300,150 390,112 470,82 540,58 540,232 440,290 360,268" fill="var(--stone)"/>
    </svg>
    <div class="brand">
      <div class="brand__name"><span class="brand__mark"></span>Lumineaux</div>
      <p class="brand__tagline">Cabinet de conseil en<br>aménagement intérieur</p>
    </div>
  </section>

  <section class="card card--back" aria-label="Verso coordonnées">
    <svg class="card__pattern" role="img" aria-label="Motif géométrique de triangles gris" viewBox="0 0 540 340">
      <polygon points="330,130 420,100 480,70 540,48 540,250 430,310 360,278" fill="var(--stone)"/>
    </svg>
    <div class="brand">
      <div class="brand__name"><span class="brand__mark"></span>Lumineaux</div>
      <p class="brand__tagline">Cabinet de conseil en<br>aménagement intérieur</p>
    </div>
    <div class="rule rule--top"></div>
    <div class="person">
      <p class="person__name">Claire-Anne <span class="surname">Vostel</span></p>
      <p class="person__role">Chief Designer</p>
    </div>
    <ul class="contact">
      <li class="contact__item">
        <svg class="contact__icon" viewBox="0 0 18 18" aria-hidden="true">
          <circle cx="9" cy="9" r="9" fill="var(--brand-blue)"/>
          <rect x="4.5" y="6" width="9" height="6.5" fill="none" stroke="#fff" stroke-width="1"/>
          <polyline points="4.5,6 9,9.8 13.5,6" fill="none" stroke="#fff" stroke-width="1"/>
        </svg>
        cavostel@mailrivo.com
      </li>
      <li class="contact__item">
        <svg class="contact__icon" viewBox="0 0 18 18" aria-hidden="true">
          <circle cx="9" cy="9" r="9" fill="var(--soft-blue)"/>
          <path d="M6 5.2c.5-.4 1-.3 1.3.2l.7 1.2c.2.4.1.8-.2 1.1l-.5.4c.4.9 1.1 1.6 2 2l.4-.5c.3-.3.7-.4 1.1-.2l1.2.7c.5.3.6.8.2 1.3-.6.8-1.5 1.1-2.4.7-1.9-.8-3.4-2.3-4.2-4.2-.4-.9-.1-1.8.4-2.7z" fill="#fff"/>
        </svg>
        + 33 6 12 58 39 91
      </li>
    </ul>
    <div class="rule rule--bottom"></div>
  </section>
</main>
</body>
</html>
```